Landing Page IT Security Vendor

We need a landing page that uses our colour scheme (www.veldonguard.com). We created a draft (see attached). We do not need standard stock template design pages. Please only apply if you can design pages from scratch and try to be as close as possible to our draft. It is ok to also purchase commecrial stock pictures

Coding

Coded - Design and coding required

Number of Pages Required

1 page

```html
<!DOCTYPE html>
<html lang="en">
<head>
<meta charset="utf-8">
<title>Veldon Guard – Security Awareness Training</title>
<link href="https://fonts.googleapis.com/css2?family=Montserrat:wght@400;500;600;700&display=swap" rel="stylesheet">
<style>
:root{
  --teal:#1ebfc4;
  --teal-dark:#17a9ae;
  --orange:#f7a300;
  --orange-deep:#f58a07;
  --ink:#2f3a40;
  --muted:#4a5358;
  --band:#e3e7ea;
  --page:#f7f8f9;
  --white:#ffffff;
}
*{box-sizing:border-box;margin:0;padding:0}
html,body{width:704px;height:1200px;overflow:hidden}
body{font-family:"Montserrat",sans-serif;background:var(--page);position:relative;color:var(--ink)}
.abs{position:absolute}
.hero{left:0;top:0;width:704px;height:372px;background:var(--teal)}
.award{top:15px;display:flex;align-items:center;gap:5px;color:var(--white);font-size:5.9px;line-height:1.45;white-space:nowrap}
.award svg{flex:none}
.nav{top:17px;right:22px;display:flex;gap:8px;align-items:center;font-size:8.5px;color:var(--white);letter-spacing:.4px}
.nav .home{background:rgba(255,255,255,.25);color:#d9f5f6;padding:5px 8px;border-radius:12px}
.eyebrow{left:39px;top:99px;color:var(--white);font-size:14px;letter-spacing:1px}
.headline{left:39px;top:138px;color:var(--white);font-size:22px;line-height:29px;font-weight:400;letter-spacing:.5px;white-space:nowrap}
.demo{left:39px;top:243px;width:98px;height:25px;border-radius:13px;background:var(--white);color:#5b6b70;font-size:7.5px;letter-spacing:.4px;display:flex;align-items:center;justify-content:center}
.portrait{left:470px;top:56px;width:192px;height:291px;background:linear-gradient(180deg,#d9c2a3 0%,#a9cfc6 45%,#8fc9c0 100%);border-radius:90px 90px 0 0}
.help{left:0;width:704px;top:287px;text-align:center;color:var(--white);font-size:13.5px;font-weight:700}
.card{top:347px;width:195px;height:232px;background:var(--white);box-shadow:0 2px 8px rgba(0,0,0,.07);text-align:center;padding:16px 6px 0}
.card h3{color:var(--orange);font-size:10px;line-height:12.8px;font-weight:700;height:44px;white-space:nowrap}
.card .lead{font-size:9px;line-height:12.4px;color:var(--ink);margin-top:2px;letter-spacing:.2px;padding:0 6px}
.card .body{font-size:6.2px;line-height:11.3px;color:var(--muted);margin-top:17px;padding:0 6px}
.card .btn{position:absolute;left:31px;bottom:18px;width:133px;height:25px;border-radius:13px;background:linear-gradient(90deg,var(--orange),var(--orange-deep));color:var(--white);font-size:7.5px;letter-spacing:.5px;display:flex;align-items:center;justify-content:center}
.band{left:0;top:628px;width:704px;height:62px;background:var(--band);display:flex;align-items:center;justify-content:center;gap:16px}
.band p{font-size:11px;font-weight:600;color:var(--ink)}
.band .learn{display:flex;align-items:center;gap:8px;background:var(--teal);color:var(--white);font-size:7.5px;height:24px;padding:0 19px 0 8px;border-radius:13px}
.trust{left:72px;top:734px;width:330px}
.trust h2{font-size:14.5px;font-weight:400;line-height:18.5px;color:var(--ink);white-space:nowrap}
.trust p{font-size:7px;line-height:11.3px;color:var(--muted);margin-top:11px}
.cta{left:72px;top:900px;width:210px;height:24px;border-radius:13px;background:linear-gradient(90deg,var(--orange),var(--orange-deep));color:var(--white);font-size:7.3px;letter-spacing:.4px;display:flex;align-items:center;justify-content:center}
.clients{left:420px;top:731px;width:212px;height:199px;background:var(--white);box-shadow:0 2px 8px rgba(0,0,0,.06);display:grid;grid-template-columns:1fr 1fr;gap:7px;padding:10px}
.client{display:flex;align-items:center;justify-content:center;font-size:9.5px;font-weight:700;color:var(--ink);border:1px solid #e6e9eb;border-radius:2px}
.footer{left:0;top:972px;width:704px;height:228px;background:var(--teal);color:var(--white)}
.footer h4{font-size:9.5px;font-weight:700;letter-spacing:.2px}
.footer .col{position:absolute;font-size:8px;line-height:12.3px}
.rule{left:50px;top:154px;width:604px;height:1px;background:rgba(255,255,255,.55)}
.brand{left:54px;top:172px;display:flex;align-items:center;gap:5px;font-size:10px;font-weight:700}
.rights{left:54px;top:201px;font-size:7px}
.badge{top:174px;width:34px;height:34px;background:rgba(255,255,255,.28)}
.up{left:680px;top:212px}
</style>
</head>
<body>

<section class="hero abs">
  <div class="award abs" style="left:25px">
    <svg width="14" height="14" viewBox="0 0 14 14"><path d="M3 1h8v3a4 4 0 0 1-8 0zM1 2h2v2a2 2 0 0 1-2-2zm12 0h-2v2a2 2 0 0 0 2-2zM6 8h2v3h2v2H4v-2h2z" fill="#fff"/></svg>
    <span>In 2020, VELDON won the Cyber Security<br>Excellence Award for Best "Anti Phishing"</span>
  </div>
  <div class="award abs" style="left:179px">
    <svg width="16" height="16" viewBox="0 0 16 16"><circle cx="8" cy="8" r="6.5" fill="none" stroke="#fff" stroke-dasharray="3 2"/><path d="M8 4.5l1 2.2 2.3.2-1.8 1.5.6 2.3L8 9.5l-2.1 1.2.6-2.3-1.8-1.5 2.3-.2z" fill="#fff"/></svg>
    <span>In 2020, VELDON won the Cyber Security<br>Excellence Award for Best "Security Education Platform".</span>
  </div>
  <div class="award abs" style="left:362px">
    <svg width="16" height="16" viewBox="0 0 16 16"><circle cx="8" cy="8" r="6.5" fill="none" stroke="#fff" stroke-dasharray="3 2"/><text x="8" y="11" font-size="8" fill="#fff" text-anchor="middle" font-family="Montserrat,sans-serif">1</text></svg>
    <span>2020 Gold Winner "Cyber Security Education<br>and Training" In the Secure Tech Buyers Review</span>
  </div>
  <nav class="nav abs"><span class="home">Home</span><span>Solution ▾</span></nav>

  <div class="portrait abs" role="img" aria-label="Photo of a smiling woman holding a tablet"></div>

  <p class="eyebrow abs">CYBER SECURITY STARTS WITH PEOPLE</p>
  <h1 class="headline abs">TRAIN YOUR STAFF WITH<br>VELDON AND IMPROVE CYBER<br>SECURITY AWARENESS</h1>
  <a class="demo abs">Request a demo</a>

  <h2 class="help abs">HOW CAN WE HELP?</h2>
  <svg class="abs" style="left:0;top:304px" width="704" height="46" viewBox="0 0 704 46">
    <g fill="none" stroke="#fff" stroke-width=".7" stroke-dasharray="2 1.5">
      <path d="M352 2v42M148 15h409M148 15v29M557 15v29"/>
    </g>
    <g fill="#fff"><circle cx="148" cy="44" r="3"/><circle cx="352" cy="44" r="3"/><circle cx="557" cy="44" r="3"/></g>
  </svg>
</section>

<article class="card abs" style="left:49px">
  <h3>IMPORT OUR TRAINING<br>COURSES IN YOUR LMS</h3>
  <p class="lead">Buy out of the box or custom tailored security courses you can import in your elearning (SCORM)</p>
  <p class="body">Veldon offers 250 fully customizable training modules in +30 languages. Games, videos, exams, posters, offline, micro-training and much more!</p>
  <a class="btn">EXPLORE OUR TRAINING</a>
</article>
<article class="card abs" style="left:254px">
  <h3>LET US DEVELOP A SECURITY<br>AWARENESS PROGRAM</h3>
  <p class="lead">VELDON Guard will assist you in improving security awareness - with money back gurantee!</p>
  <p class="body">Our security awareness specialists will identify risky users via phising simulations. We develop a tailored awareness program and reduce your exposure to social hacking.</p>
  <a class="btn">EXPLORE OUR SERVICES</a>
</article>
<article class="card abs" style="left:460px">
  <h3>INSTALL THE VELDON SOFTWARE<br>ON-PREMISE OR GET ACCESS<br>TO THE SAAS VERSION</h3>
  <p class="lead">Buy out of the box or custom tailored security courses you can import in your elearning (SCORM)</p>
  <p class="body">The VELDON software can be installed on-premise or in the cloud. If you don't want to deal with the installation we onboard you in 24 h on our SAAS!</p>
  <a class="btn">EXPLORE OUR SOFTWARE</a>
</article>

<section class="band abs">
  <p>VELDON is also available for MSSP</p>
  <a class="learn">
    <svg width="14" height="14" viewBox="0 0 14 14"><circle cx="7" cy="7" r="6" fill="none" stroke="#fff"/><path d="M7 6v4M7 4v.8" stroke="#fff" stroke-width="1.2"/></svg>
    LEARN MORE
  </a>
</section>

<section class="trust abs">
  <h2>Already over 12,000,000<br>Employees worldwide trust and use VELDON.</h2>
  <p style="margin-top:24px">Veldon Guard is a name you can trust! Because we have won countless awards since 2015 and help well-known brands around the world.</p>
  <p>You know you're getting a quality solution with us.</p>
  <p>Our services can be customized to fit your needs and company size.<br>Talk to our team to learn more.</p>
</section>
<a class="cta abs">GET IN TOUCH WITH THE VELDON TEAM NOW!</a>

<div class="clients abs">
  <span class="client">Norvia</span><span class="client">Aerolith</span>
  <span class="client">Railnord</span><span class="client">Kestrel</span>
  <span class="client">Hausmark</span><span class="client">Tessaro</span>
  <span class="client">Chemora</span><span class="client">Millhaven</span>
  <span class="client" style="grid-column:span 2">Vantis Informatik</span>
</div>

<footer class="footer abs">
  <h4 class="abs" style="left:71px;top:43px">CONTACTS</h4>
  <div class="col" style="left:71px;top:66px">Address: Europe<br>Veldon Guard AG<br>Seeweg 12 | 6301 Ostbach | Switzerland</div>
  <div class="col" style="left:257px;top:54px">Address: North America<br>Veldon Guard USA<br>4410 Harlow Ave<br>Suite 210<br>Cedar Park, TX 78613</div>
  <div class="col" style="left:386px;top:54px">Phone Global: +41 44 000 12 34<br>Phone USA: +1-512-555-0142<br>Phone USA Support: +1-512-555-0187<br>Phone France: +33 600 555 210<br>Phone UK: +44 (0) 7700 900412</div>
  <h4 class="abs" style="left:579px;top:43px">LANGUAGE</h4>
  <div class="col" style="left:579px;top:62px;font-size:7px">English &nbsp;&nbsp; ▾</div>

  <div class="rule abs"></div>
  <div class="brand abs"><span style="width:10px;height:10px;border-radius:50%;background:var(--white)"></span>Veldon</div>
  <div class="rights abs">All Rights Reserved 2020</div>

  <div class="badge abs" style="left:170px"></div>
  <div class="badge abs" style="left:219px;border-radius:50%"></div>
  <div class="badge abs" style="left:266px"></div>
  <div class="badge abs" style="left:312px"></div>
  <div class="badge abs" style="left:358px"></div>
  <div class="badge abs" style="left:401px;height:20px;top:181px;border-radius:4px"></div>
  <div class="badge abs" style="left:450px"></div>
  <div class="badge abs" style="left:494px;border-radius:4px"></div>
  <div class="badge abs" style="left:540px;width:56px;height:22px;top:180px;border-radius:11px"></div>
  <div class="badge abs" style="left:607px;border-radius:50%"></div>
  <svg class="up abs" width="12" height="12" viewBox="0 0 12 12"><path d="M6 11V2M2 6l4-4 4 4" fill="none" stroke="#2f3a40" stroke-width="1.4"/></svg>
</footer>

</body>
</html>
```